New Business Card Design Project

We would like a business card that represents the sale of boat, home, auto, and life insurance.

The logo can change colors to meet the look of the design if needed.

Industry/Entity Type

Business

```html
<!DOCTYPE html>
<html lang="en">
<head>
<meta charset="UTF-8">
<title>Altura Financial – Business Card</title>
<link rel="stylesheet" href="https://fonts.googleapis.com/css2?family=Questrial&display=swap">
<style>
  :root {
    --teal: #3e7186;
    --teal-dark: #2f5d70;
    --ink: #2f3a44;
    --grey: #7b7f84;
    --grey-light: #c9ccd0;
    --black: #111418;
    --paper: #fbfbfb;
    --page: #d9d9db;
    --white: #ffffff;
  }
  * { box-sizing: border-box; margin: 0; padding: 0; }
  html, body { width: 883px; height: 1200px; overflow: hidden; }
  body {
    background: var(--page);
    font-family: "Questrial", "Century Gothic", sans-serif;
    position: relative;
  }
  .card {
    position: absolute;
    left: 91px;
    width: 700px;
    height: 392px;
    overflow: hidden;
    box-shadow: 0 3px 10px rgba(0,0,0,0.18);
  }
  .card--front { top: 178px; background: var(--teal); }
  .card--back { top: 610px; background: var(--paper); }

  /* front */
  .front-lockup {
    position: absolute;
    left: 0; right: 0;
    top: 160px;
    text-align: center;
    color: var(--white);
  }
  .front-lockup .brand-name {
    font-size: 50px;
    letter-spacing: 6px;
    line-height: 1;
  }
  .front-lockup .brand-name span {
    display: block;
    font-size: 31px;
    letter-spacing: 9px;
    margin-top: 6px;
  }
  .front-lockup .tagline {
    font-size: 22px;
    letter-spacing: 2px;
    margin-top: 10px;
  }

  /* back */
  .services-art {
    position: absolute;
    left: 290px; top: 70px;
    width: 250px; height: 290px;
    border-radius: 50%;
    background: radial-gradient(circle at 50% 45%, rgba(190,197,206,0.55), rgba(220,224,229,0.25) 60%, rgba(251,251,251,0) 72%);
  }
  .back-lockup {
    position: absolute;
    left: 36px; top: 48px;
    color: var(--ink);
  }
  .back-lockup .brand-name {
    font-size: 38px;
    letter-spacing: 5px;
    line-height: 1;
  }
  .back-lockup .brand-name span {
    display: block;
    font-size: 24px;
    letter-spacing: 7px;
    margin-top: 4px;
    padding-left: 16px;
  }
  .back-lockup .tagline {
    font-size: 17px;
    letter-spacing: 1px;
    margin-top: 6px;
  }
  .divider-bars span {
    position: absolute;
    top: 208px;
    height: 6px;
  }
  .bar-teal { left: 36px; width: 252px; background: var(--teal); }
  .bar-grey { left: 294px; width: 98px; background: var(--grey); }
  .bar-light { left: 398px; width: 98px; background: var(--grey-light); }
  .bar-black { left: 502px; width: 156px; background: var(--black); }

  .contact-list {
    position: absolute;
    left: 36px; top: 224px;
    list-style: none;
    font-size: 18px;
    color: var(--black);
  }
  .contact-list li {
    display: flex;
    align-items: center;
    height: 23px;
  }
  .contact-list svg { width: 14px; height: 14px; margin-right: 18px; fill: var(--ink); }

  .person {
    position: absolute;
    right: 42px; top: 146px;
    text-align: right;
  }
  .person .name { font-size: 28px; color: var(--teal); line-height: 1; }
  .person .role { font-size: 17px; color: var(--ink); margin-top: 2px; }

  .address {
    position: absolute;
    right: 42px; top: 236px;
    display: flex;
    align-items: flex-start;
    gap: 10px;
    color: var(--teal);
    font-size: 17px;
    text-align: right;
    line-height: 23px;
  }
  .address svg { width: 12px; height: 16px; fill: var(--black); margin-top: 3px; }

  .back-waves { position: absolute; left: 0; bottom: 0; width: 700px; height: 80px; }
</style>
</head>
<body>

<section class="card card--front" aria-label="Card front">
  <div class="front-lockup">
    <div class="brand-name">ALTURA<span>financial</span></div>
    <div class="tagline">investments &amp; insurance</div>
  </div>
</section>

<section class="card card--back" aria-label="Card back">
  <div class="services-art" role="img" aria-label="Faint illustration of a house, car, boat and couple representing home, auto, boat and life insurance"></div>

  <div class="back-lockup">
    <div class="brand-name">ALTURA<span>financial</span></div>
    <div class="tagline">investments &amp; insurance</div>
  </div>

  <div class="divider-bars">
    <span class="bar-teal"></span>
    <span class="bar-grey"></span>
    <span class="bar-light"></span>
    <span class="bar-black"></span>
  </div>

  <ul class="contact-list">
    <li><svg viewBox="0 0 14 14"><rect x="1" y="4" width="12" height="8" rx="1.5"/><rect x="3" y="1" width="8" height="3" rx="1"/></svg>0123 456 789</li>
    <li><svg viewBox="0 0 14 14"><path d="M4 0h6a1.5 1.5 0 0 1 1.5 1.5v11A1.5 1.5 0 0 1 10 14H4a1.5 1.5 0 0 1-1.5-1.5v-11A1.5 1.5 0 0 1 4 0zm0.5 2v9h5V2z"/></svg>0123 456 789</li>
    <li><svg viewBox="0 0 14 14"><path d="M1 3h12v8H1z M1 3l6 5 6-5" stroke="#fff" stroke-width="1"/></svg>youremail@mail.com</li>
    <li><svg viewBox="0 0 14 14"><circle cx="7" cy="7" r="6"/></svg>www.yourwebsite.com</li>
  </ul>

  <div class="person">
    <div class="name">your name</div>
    <div class="role">designation</div>
  </div>

  <div class="address">
    <div>address (street address<br>suite number, city, state, zip</div>
    <svg viewBox="0 0 12 16"><path d="M6 0a6 6 0 0 1 6 6c0 4-6 10-6 10S0 10 0 6a6 6 0 0 1 6-6zm0 3.5a2.5 2.5 0 1 0 0 5 2.5 2.5 0 0 0 0-5z"/></svg>
  </div>

  <svg class="back-waves" viewBox="0 0 700 80" preserveAspectRatio="none" aria-hidden="true">
    <path d="M0 20 C200 6 450 2 700 12 L700 80 L0 80 Z" fill="var(--grey)"/>
    <path d="M0 31 C200 16 450 12 700 20 L700 80 L0 80 Z" fill="var(--white)"/>
    <path d="M0 39 C200 24 450 20 700 26" stroke="var(--grey)" stroke-width="2" fill="none"/>
    <path d="M0 47 C220 32 460 26 700 30 L700 80 L0 80 Z" fill="var(--teal)"/>
  </svg>
</section>

</body>
</html>
```